cleaning service

we are a cleaning company,

we have a current flyer but its very dull

I have attached it, can we make it look modern, maybe add pictures and colour

```html
<!DOCTYPE html>
<html lang="en">
<head>
<meta charset="utf-8">
<title>Mara's Cleaning Services – Special Offer</title>
<link href="https://fonts.googleapis.com/css2?family=Ubuntu:wght@400;500;700&display=swap" rel="stylesheet">
<style>
  :root {
    --navy: #1a2651;
    --green: #63bf72;
    --red: #c8321e;
    --white: #ffffff;
    --paper-top: #ffffff;
    --paper-bottom: #eceef5;
    --mesh: #b9cde3;
  }
  * { box-sizing: border-box; margin: 0; padding: 0; }
  html, body { width: 1200px; height: 848px; overflow: hidden; }
  body {
    font-family: "Ubuntu", sans-serif;
    background: radial-gradient(ellipse at 55% 30%, var(--paper-top) 0%, var(--paper-bottom) 100%);
    position: relative;
    color: var(--navy);
  }
  .flyer { position: relative; width: 1200px; height: 848px; }

  .mesh-band {
    position: absolute; left: 0; top: 312px; width: 1200px; height: 300px;
    background: linear-gradient(180deg, rgba(185,205,227,0) 0%, rgba(185,205,227,0.28) 45%, rgba(185,205,227,0) 100%);
  }

  .badge { position: absolute; left: 50px; width: 140px; height: 120px; }
  .badge--intro { top: 48px; }
  .badge--custom { top: 184px; }
  .badge-name {
    position: absolute; left: 16px; top: 48px; width: 100px; text-align: center;
    font-weight: 700; font-size: 17px;
  }
  .badge--intro .badge-name { color: var(--navy); }
  .badge--custom .badge-name { color: var(--white); }

  .panel {
    position: absolute; left: 211px; width: 875px;
    border-radius: 21px; font-size: 18px;
  }
  .panel--intro {
    top: 52px; height: 113px; background: var(--navy); color: var(--white);
    padding: 14px 20px; line-height: 29px; font-weight: 500;
  }
  .panel--custom {
    top: 198px; height: 113px; background: var(--white);
    border: 1.5px solid var(--navy); color: var(--navy);
    padding: 15px 12px; line-height: 25.6px; font-weight: 500;
  }

  .offer { position: absolute; left: 460px; top: 325px; width: 300px; height: 230px; }
  .offer-text {
    position: absolute; left: 482px; top: 370px; width: 216px;
    text-align: center; color: var(--white); font-weight: 700;
  }
  .offer-percent { font-size: 70px; line-height: 72px; letter-spacing: -1px; }
  .offer-label { font-size: 28px; line-height: 30px; margin-top: 6px; }

  .call {
    position: absolute; left: 0; top: 562px; width: 1170px; text-align: center;
    font-size: 41px; font-weight: 500; color: var(--navy);
  }
  .call strong { font-weight: 700; }

  .perks {
    position: absolute; left: 100px; top: 620px; width: 1000px; text-align: center;
    color: var(--red); font-size: 19px; line-height: 25px; font-weight: 500;
  }
  .perks .perks-strong { font-weight: 700; }

  .eco {
    position: absolute; left: 0; top: 688px; width: 1200px; height: 160px;
    background: var(--green); color: var(--white);
    padding: 12px 60px 0 72px; font-size: 20px; line-height: 24.6px;
  }
</style>
</head>
<body>
<main class="flyer">
  <div class="mesh-band" role="img" aria-label="Faint network of connected dots and lines across the middle of the flyer"></div>

  <div class="badge badge--intro">
    <svg width="140" height="120" viewBox="0 0 140 120" aria-hidden="true">
      <circle cx="7" cy="6" r="5" fill="var(--green)"/>
      <circle cx="44" cy="37" r="31" fill="var(--green)"/>
      <circle cx="66" cy="59" r="52" fill="var(--green)"/>
      <circle cx="129" cy="73" r="9" fill="var(--green)"/>
    </svg>
    <span class="badge-name">Mara's</span>
  </div>

  <div class="panel panel--intro">
    Mara's Cleaning Services offers professional cleaning services to make your home look its very best. From cleaning sinks, baths and tiles to polishing windows, our cleaners have the expertise to deal with every cleaning challenge.
  </div>

  <div class="badge badge--custom">
    <svg width="140" height="120" viewBox="0 0 140 120" aria-hidden="true">
      <circle cx="7" cy="6" r="5" fill="var(--navy)"/>
      <circle cx="44" cy="37" r="31" fill="var(--navy)"/>
      <circle cx="66" cy="59" r="52" fill="var(--navy)"/>
      <circle cx="129" cy="73" r="9" fill="var(--navy)"/>
    </svg>
    <span class="badge-name">Mara's</span>
  </div>

  <div class="panel panel--custom">
    Let me customise a cleaning service programme to suit your individual needs and your budget. Whether you require a regular service (daily, weekly or monthly) or just a one-off service, you can count on Mara's Cleaning services for a cleaning service at excellent rates.
  </div>

  <svg class="offer" viewBox="0 0 300 230" aria-hidden="true">
    <circle cx="65" cy="64" r="57" fill="var(--navy)"/>
    <circle cx="130" cy="111" r="108" fill="var(--navy)"/>
    <circle cx="260" cy="140" r="18" fill="var(--navy)"/>
  </svg>
  <div class="offer-text">
    <div class="offer-percent">20%</div>
    <div class="offer-label">SPECIAL<br>OFFER</div>
  </div>

  <p class="call">Please call us on <strong>07700900123</strong> to beat any price</p>

  <p class="perks">
    We can integrate the cleaning services with the newspaper delivery services and as well are offering a<br>
    <span class="perks-strong">20% off for all our newspaper customers and £50 for introducing us to your family and friends.</span>
  </p>

  <section class="eco">
    In addition, Mara's Cleaning Services believes that the products we use really matter. All the products we use are natural and non-toxic, which makes them healthier for your home and safer for the local London environment.<br>
    I have personally research all our house cleaning products to ensure they are non-toxic, biodegradable and not tested on animals.
  </section>
</main>
</body>
</html>
```